Design a Banner for Australian Football Rankmaster News

I need a logo / banner for a site called "Rankmaster News". It's a site about Australian Rules Football (ZKP), and the site will contain news about rankmaster competition points and movements.

I've attached a mockup of the site.

```html
<!DOCTYPE html>
<html lang="en">
<head>
<meta charset="utf-8">
<title>Rankmaster News – Banner</title>
<link rel="stylesheet" href="https://fonts.googleapis.com/css2?family=Graduate&display=swap">
<style>
  :root {
    --grass-light: #5fae2e;
    --grass-mid: #3f8a1f;
    --grass-dark: #1f4f10;
    --ball-light: #f0573f;
    --ball-mid: #d2301f;
    --ball-dark: #8e1a10;
    --band: rgba(0, 0, 0, 0.55);
    --title: #ffffff;
  }
  html, body {
    margin: 0;
    padding: 0;
    overflow: hidden;
    background: #ffffff;
  }
  .banner {
    position: relative;
    width: 1200px;
    height: 240px;
    overflow: hidden;
  }
  .banner svg {
    display: block;
  }
  .site-name {
    font-family: "Graduate", "Georgia", serif;
    font-weight: 400;
    fill: var(--title);
  }
</style>
</head>
<body>
  <header class="banner">
    <svg width="1200" height="240" viewBox="0 0 1200 240" xmlns="http://www.w3.org/2000/svg">
      <defs>
        <radialGradient id="grass-tone" cx="0.35" cy="0.3" r="0.9">
          <stop offset="0" stop-color="var(--grass-light)"/>
          <stop offset="0.55" stop-color="var(--grass-mid)"/>
          <stop offset="1" stop-color="var(--grass-dark)"/>
        </radialGradient>
        <radialGradient id="ball-tone" cx="0.4" cy="0.35" r="0.75">
          <stop offset="0" stop-color="var(--ball-light)"/>
          <stop offset="0.6" stop-color="var(--ball-mid)"/>
          <stop offset="1" stop-color="var(--ball-dark)"/>
        </radialGradient>
      </defs>

      <rect class="grass-field" role="img" aria-label="Close-up photo of a green grass football field"
            x="0" y="0" width="1200" height="240" fill="url(#grass-tone)"/>

      <ellipse class="football" role="img" aria-label="Photo of a red Australian Rules football resting on the grass"
               cx="960" cy="70" rx="290" ry="150" transform="rotate(-12 960 70)" fill="url(#ball-tone)"/>

      <rect class="title-band" x="0" y="97" width="1200" height="92" fill="var(--band)"/>

      <text class="site-name" x="40" y="172" font-size="80" textLength="1120" lengthAdjust="spacingAndGlyphs">RANKMASTER NEWS</text>
    </svg>
  </header>
</body>
</html>
```